Painting Company Business Card

Brightwell Painting needs a new business card. See attachments for our logo and current card as an example.
We want to utilize the same colors in the logo, and keep all the information that is currently on it. Just need an updated and modern design.
We are open to loosing the Association Logos if it means a better design.
We are also entertaining a spot for a picture of a headshot of the person listed on the card. Head shot can be finished later.

```html
<!DOCTYPE html>
<html lang="en">
<head>
<meta charset="utf-8">
<title>Brightwell Painting – Business Card</title>
<link href="https://fonts.googleapis.com/css2?family=Roboto:wght@400;700&display=swap" rel="stylesheet">
<style>
  :root {
    --backdrop: #5b5b5d;
    --card: #ffffff;
    --forest: #3f4732;
    --brick: #6e3630;
    --ink-soft: #3c3c3c;
    --on-dark: #ffffff;
  }
  * { margin: 0; padding: 0; box-sizing: border-box; }
  html, body {
    width: 1074px; height: 1200px; overflow: hidden;
    background: var(--backdrop);
    font-family: "Roboto", Arial, sans-serif;
  }
  .canvas { position: relative; width: 1074px; height: 1200px; }

  .card {
    position: absolute; left: 101px; width: 876px;
    background: var(--card);
    box-shadow: 10px 12px 18px rgba(0,0,0,0.35);
    overflow: hidden;
  }
  .card--front { top: 91px; height: 500px; }
  .card--back  { top: 612px; height: 501px; }

  /* front */
  .front-brand {
    position: absolute; left: 0; right: 0; top: 180px;
    display: flex; justify-content: center; align-items: center; gap: 18px;
  }
  .brand-mark {
    width: 26px; height: 26px; background: var(--forest);
  }
  .brand-name {
    color: var(--forest); font-weight: 700; line-height: 1.02;
    font-size: 60px; letter-spacing: 0.5px;
  }
  .front-band {
    position: absolute; left: 0; right: 0; top: 417px; height: 83px;
    background: var(--forest);
    display: flex; justify-content: center; align-items: center;
    padding-bottom: 14px;
  }
  .web-address {
    color: var(--on-dark); font-size: 22px; letter-spacing: 4.4px;
  }

  /* back */
  .accent-bar {
    position: absolute; left: 0; top: 70px; width: 31px; height: 73px;
    background: var(--brick);
  }
  .person { position: absolute; left: 60px; top: 71px; }
  .person-name {
    color: var(--forest); font-weight: 700; font-size: 29px; letter-spacing: 2.6px;
  }
  .person-title {
    margin-top: 6px; color: var(--ink-soft); font-size: 21px; letter-spacing: 1.6px;
  }
  .back-brand {
    position: absolute; left: 600px; top: 96px;
    display: flex; align-items: center; gap: 12px;
  }
  .back-brand .brand-mark { width: 16px; height: 16px; }
  .back-brand .brand-name { font-size: 36px; }

  .back-band {
    position: absolute; left: 0; right: 0; top: 224px; height: 259px;
    background: var(--forest); color: var(--on-dark);
  }
  .contact-list { position: absolute; left: 59px; top: 86px; list-style: none; }
  .contact-item {
    display: flex; align-items: center; gap: 22px; height: 37px; margin-bottom: 13px;
    font-size: 22px; letter-spacing: 2px; white-space: nowrap;
  }
  .contact-icon { width: 37px; height: 37px; flex: none; }
  .band-divider {
    position: absolute; left: 468px; top: 44px; width: 3px; height: 168px;
    background: var(--on-dark);
  }
  .services { position: absolute; left: 507px; top: 96px; font-size: 22px; }
  .service-row { height: 46px; display: flex; align-items: center; }
  .service-row .dot { margin: 0 8px 0 10px; font-size: 16px; }
</style>
</head>
<body>
<div class="canvas">

  <section class="card card--front">
    <div class="front-brand">
      <span class="brand-mark"></span>
      <span class="brand-name">Brightwell<br>Painting</span>
    </div>
    <div class="front-band">
      <span class="web-address">www.brightwellpainting.com</span>
    </div>
  </section>

  <section class="card card--back">
    <div class="accent-bar"></div>
    <div class="person">
      <div class="person-name">DANIEL HARPER</div>
      <div class="person-title">Quality Manager</div>
    </div>
    <div class="back-brand">
      <span class="brand-mark"></span>
      <span class="brand-name">Brightwell<br>Painting</span>
    </div>

    <div class="back-band">
      <ul class="contact-list">
        <li class="contact-item">
          <svg class="contact-icon" viewBox="0 0 37 37" aria-hidden="true">
            <circle cx="18.5" cy="18.5" r="17" fill="none" stroke="#fff" stroke-width="2"/>
            <path d="M13 10.5c1-.8 2-.6 2.6.3l1.6 2.6c.5.8.3 1.6-.4 2.2l-1.1.9c.8 2 2.3 3.6 4.3 4.6l1-1.1c.6-.7 1.5-.8 2.3-.3l2.5 1.7c.9.6 1 1.7.2 2.6l-1.2 1.3c-1 1-2.6 1.3-4 .7-4.6-2-8-5.5-9.6-10.1-.5-1.4-.1-2.9 1-3.9z" fill="#fff"/>
          </svg>
          <span>262 555 0147</span>
        </li>
        <li class="contact-item">
          <svg class="contact-icon" viewBox="0 0 37 37" aria-hidden="true">
            <circle cx="18.5" cy="18.5" r="17" fill="none" stroke="#fff" stroke-width="2"/>
            <rect x="10" y="13" width="17" height="12" rx="1" fill="#fff"/>
            <path d="M10.5 13.5l8 6.5 8-6.5" fill="none" stroke="#3f4732" stroke-width="1.4"/>
          </svg>
          <span>daniel@brightwell.com</span>
        </li>
      </ul>
      <div class="band-divider"></div>
      <div class="services">
        <div class="service-row">Exterior Painting<span class="dot">●</span>Carpentry</div>
        <div class="service-row">Interior Painting<span class="dot">●</span>Drywall</div>
      </div>
    </div>
  </section>

</div>
</body>
</html>
```